Website Design Project

KEL VISA is looking for a professional designer who would re-design our current website www.bordwellpassage.com.
KEL provides immigration and visa services to the US in these markets: Slovakia, Czech republic and USA. We would like to target Poland and Russia as well.
Who are we: KEL is Dubrik & Helmsley international law firm with offices in New York, Bratislava and Prague. We are licensed in several jurisdiction such as New York, England and Wales, and Slovakia.
Additionally, we are offering online products in our E-shop, such as E-books, E-brochures, DVD's regarding visa and immigration opportunities into United States.
Our targeted audience is: young students who want to study in the US, young professionals looking for employment in the US, investors who want to invest to the US, people looking to get their green card (permanent residency in the US), etc.
Our new design: should look professional, communicate financial safety, professional services, increase sales, but also feel emotional for people who are looking forward to start their new life in the United States.
Updates

Dear Designers, 

we have changed our project from refundable to committed! 

Cant wait to see your designs! 

Thanks! 

KEL VISA 

Designers! 

We have attached pictures od old NY so you may wanna work with them! 

Target Market(s)

USA, Slovakia, Czech Republic

Industry/Entity Type

Financial

Requirements
Nice to have
• 1) pictures of old New York, Tarrow Quay.
2) pictures of the US
Should not have
• KEL VISA is operated by law form Dubrik & Helmsley. We are not looking for boring, old fashioned and profesional website for "legal practitioners". No dark colors, no brown color, no dark green color. it should look light and fresh.

KEL VISA is fresh, new, modern, professional and flexible TEAM of YOUNG and SMART immigration lawyers who want to make a difference. Our website MUST reflect our philosophy. "Success is all about people that we meet and the things we create with them".

```html
<!DOCTYPE html>
<html lang="en">
<head>
<meta charset="utf-8">
<title>KEL VISA – Visas to the U.S. and U.S. Immigration</title>
<link href="https://fonts.googleapis.com/css2?family=Arimo:wght@400;700&family=PT+Sans:wght@400;700&display=swap" rel="stylesheet">
<style>
:root{
  --navy:#0b3468;
  --nav-divider:#2a4f82;
  --brand-red:#8c1a16;
  --heading-red:#7b1410;
  --orange:#e2991a;
  --link-blue:#1a4fa0;
  --bullet-red:#c0281c;
  --text:#333;
  --muted:#777;
  --line:#ddd;
  --bg:#ececec;
  --white:#fff;
}
*{box-sizing:border-box;margin:0;padding:0}
html,body{width:986px;height:1200px;overflow:hidden}
body{background:var(--bg);font-family:"Arimo",Arial,sans-serif;color:var(--text);position:relative}
a{color:inherit;text-decoration:none}
.page{position:absolute;left:146px;top:16px;width:694px;height:1174px;background:var(--white)}
.abs{position:absolute}

.brand{left:8px;top:34px;display:flex;align-items:flex-start}
.brand-photo{width:62px;height:43px;background:linear-gradient(135deg,#cfcfcf,#777 60%,#a5a5a5)}
.brand-text{margin-left:2px}
.brand-name{font-family:"PT Sans",sans-serif;font-weight:700;font-size:19px;color:var(--navy);letter-spacing:.3px;margin:2px 0 0 4px;white-space:nowrap}
.brand-tag{display:block;margin-top:3px;background:var(--brand-red);color:var(--white);font-size:8px;padding:2px 5px;width:213px;white-space:nowrap}

.welcome{right:8px;top:38px;font-size:8px;color:var(--muted);white-space:nowrap}
.welcome a{color:var(--link-blue)}
.account-links{right:126px;top:63px;font-size:8px;color:var(--muted);white-space:nowrap}
.account-links span{margin:0 3px}
.cart{right:8px;top:56px;width:106px;height:23px;background:var(--orange);color:var(--white);font-size:8px;display:flex;align-items:center;padding-left:7px;white-space:nowrap}
.cart b{font-size:10px;margin-right:5px}

.main-nav{left:0;top:99px;width:694px;height:38px;background:var(--navy);display:flex;align-items:center;padding-left:7px;white-space:nowrap}
.main-nav a{flex:none;font-family:"PT Sans",sans-serif;color:var(--white);font-size:10.5px;padding:0 6px;border-right:1px solid var(--nav-divider);line-height:18px;white-space:nowrap}
.main-nav a:last-child{border:none}

.hero{left:0;top:137px;width:694px;height:274px;background:linear-gradient(180deg,#8c9290 0%,#6f7773 40%,#4f5a3a 70%,#7d7a62 100%)}
.slide-arrow{top:127px;width:35px;height:19px;background:#e8e8e8;border-radius:3px;display:flex;align-items:center;justify-content:center}

.intro-title{left:12px;top:424px;font-family:"PT Sans",sans-serif;font-weight:700;font-size:11px;color:var(--heading-red)}
.intro-photo{left:13px;top:447px;width:155px;height:131px;background:linear-gradient(180deg,#aebfd0 0%,#b88676 55%,#7d8f78 100%)}
.intro-text{left:13px;top:444px;width:668px;font-size:8.3px;line-height:12.4px;text-align:justify}
.intro-text p{margin-bottom:12.4px}
.intro-text .beside{margin-left:163px}
.divider{left:14px;top:714px;width:666px;height:1px;background:var(--line)}

.list-box{top:730px;height:156px;border:1px solid var(--line)}
.list-box h3{background:var(--navy);color:var(--white);font-family:"PT Sans",sans-serif;font-size:11px;height:29px;line-height:29px;padding-left:10px}
.list-box ul{list-style:none;padding:6px 0 0 6px}
.list-box li{font-size:8.3px;height:23.6px;line-height:14px;display:flex;gap:6px;white-space:nowrap}
.list-box li svg{margin-top:3px;flex:none}

.product{top:901px;width:216px;height:96px;border:1px solid #ccc;background:linear-gradient(#fff,#f1f1f1)}
.product-art{left:10px;top:12px;width:60px;height:72px;border-radius:2px}
.art-ebook{background:linear-gradient(180deg,#b57446,#8a4c28)}
.art-brochure{background:linear-gradient(180deg,#d9656a,#c9a878)}
.art-dvd{background:linear-gradient(180deg,#9ccdf0,#4a90cf)}
.product h4{left:86px;top:12px;font-family:"PT Sans",sans-serif;font-size:11px;color:var(--heading-red)}
.product p{left:86px;top:32px;width:124px;font-size:8.3px;line-height:12.5px}
.product .more{left:86px;top:78px;font-size:8.3px;color:var(--link-blue)}

.footer-col{top:1024px;font-size:8.3px;line-height:12.4px;color:var(--muted);white-space:nowrap}
.footer-col h5{font-weight:400;color:#222;font-size:8.3px;margin-bottom:6px}
.footer-col h5.tight{margin-bottom:0}
.footer-col h5.sub{margin-top:6px}
.footer-rule{left:14px;top:1139px;width:666px;height:1px;background:var(--line)}
.legal{left:16px;top:1152px;font-size:8.3px;color:#222}
.social{right:12px;top:1149px;display:flex;gap:6px}
.social span{width:12px;height:12px}
</style>
</head>
<body>
<div class="page">
  <header>
    <a class="brand abs" href="#">
      <div class="brand-photo" role="img" aria-label="Statue of Liberty head in grey tones"></div>
      <div class="brand-text">
        <div class="brand-name">BORDWELL PASSAGE</div>
        <span class="brand-tag">Immigration Attorneys, US Visa, US Green Card, ESTA</span>
      </div>
    </a>
    <div class="welcome abs">Welcome visitor you can <a href="#">Login</a> or <a href="#">Create an account</a></div>
    <div class="account-links abs">Wish list (0)<span>|</span>My account<span>|</span>Shopping cart<span>|</span>Checkout</div>
    <a class="cart abs" href="#"><b>Cart:</b> 0 item(s) - $0.00</a>
  </header>

  <nav class="main-nav abs">
    <a href="#">Consultation</a><a href="#">Visitors Visas</a><a href="#">Work Visas</a><a href="#">Business Visas</a><a href="#">Family Visas</a><a href="#">Student Visas</a><a href="#">Green Card</a><a href="#">Visa Forms</a><a href="#">KEL E-shop</a><a href="#">Visa News</a>
  </nav>

  <section class="hero abs" role="img" aria-label="Aerial view of Liberty Island with the statue, surrounded by harbour water and boats">
    <div class="slide-arrow abs" style="left:8px"><svg width="10" height="10"><path d="M7 1 3 5l4 4" stroke="#999" stroke-width="2" fill="none"/></svg></div>
    <div class="slide-arrow abs" style="right:9px"><svg width="10" height="10"><path d="M3 1l4 4-4 4" stroke="#999" stroke-width="2" fill="none"/></svg></div>
  </section>

  <h2 class="intro-title abs">VISAS TO THE U.S. AND U.S. IMMIGRATION</h2>
  <div class="intro-photo abs" role="img" aria-label="Historic red brick immigration hall on Tarrow Quay"></div>
  <div class="intro-text abs">
    <p class="beside">KEL Visa and Immigration USA aids travelers in the process of obtaining green cards or different visas to enter the United States. A traveler may obtain a visa to the United States from a consulate of the USA, and must show it upon entry to the country. The immigration lawyer at passport control can authorize the visa holder entry, determine the length of stay, or deny entry to the U.S.</p>
    <p class="beside">Bordwell Passage is experienced in different visas for the United States. We are here for assistance with investor, family, student visas, and other travel visa questions. Contact us today if you are unsure of which visa you need for the United States, and we will arrange the process for you.</p>
    <p class="beside">For students we offer three different types of visas: F1, J1, M1. For studying at a high school or college, a F1 visa is needed. The J1 visa is ideal for attending a college or university, while employed, and the M1 visa should be used by any students attending a college or university. These visas are all temporary and will need to be renewed each term.</p>
    <p>The E visa is for individuals who are investing in a business for a substantial profit. This visa to the U.S will only be approved for citizens of partnering countries. We are currently preparing Ebooks for more information and guides on investment visas and other assistance.</p>
    <p>If you are traveling with a school, family, or tour group we offer visas to the United States for large groups and associations. We are aided by the experienced attorneys at Dubrik &amp; Helmsley.</p>
    <p>Dubrik &amp; Helmsley is a leading international law firm dedicated to delivering the most innovative solutions to our clients. We practice all aspects of U.S. law with a special focus on immigration law. Headquartered in New York, NY, and with branch offices in Bratislava, and Prague, Dubrik &amp; Helmsley can handle U.S. cases and transactions anywhere within and outside the U.S. by using the latest legal and tax architecture.</p>
  </div>
  <div class="divider abs"></div>

  <section class="list-box abs" style="left:14px;width:226px">
    <h3>RECENT POSTS</h3>
    <ul>
      <li><svg width="5" height="7"><path d="M1 1l3 2.5L1 6" stroke="#c0281c" stroke-width="1.6" fill="none"/></svg>Applying for Your US Passport</li>
      <li><svg width="5" height="7"><path d="M1 1l3 2.5L1 6" stroke="#c0281c" stroke-width="1.6" fill="none"/></svg>E-11 Immigrant Visa to the US</li>
      <li><svg width="5" height="7"><path d="M1 1l3 2.5L1 6" stroke="#c0281c" stroke-width="1.6" fill="none"/></svg>Daniel Harlow and his Immigration Policy</li>
      <li><svg width="5" height="7"><path d="M1 1l3 2.5L1 6" stroke="#c0281c" stroke-width="1.6" fill="none"/></svg>How to Get a Student Visa to the US</li>
      <li><svg width="5" height="7"><path d="M1 1l3 2.5L1 6" stroke="#c0281c" stroke-width="1.6" fill="none"/></svg>A Probable Deal on Immigration Reform in the US?</li>
    </ul>
  </section>
  <section class="list-box abs" style="left:248px;width:434px">
    <h3>MOST VIEWED</h3>
    <ul>
      <li><svg width="5" height="7"><path d="M1 1l3 2.5L1 6" stroke="#c0281c" stroke-width="1.6" fill="none"/></svg>Visa to the U.S.</li>
      <li><svg width="5" height="7"><path d="M1 1l3 2.5L1 6" stroke="#c0281c" stroke-width="1.6" fill="none"/></svg>E-2 Visa and E-1 Visa – How to Become “Legal” Entrepreneur in the U.S.</li>
      <li><svg width="5" height="7"><path d="M1 1l3 2.5L1 6" stroke="#c0281c" stroke-width="1.6" fill="none"/></svg>How to Become J-1 Visa Exchange Visitor Without Paying Unnecessary Fees</li>
      <li><svg width="5" height="7"><path d="M1 1l3 2.5L1 6" stroke="#c0281c" stroke-width="1.6" fill="none"/></svg>Electronic Diversity Visa Lottery DV-2014, ONLY 3 DAYS LEFT!!!</li>
      <li><svg width="5" height="7"><path d="M1 1l3 2.5L1 6" stroke="#c0281c" stroke-width="1.6" fill="none"/></svg>E-2 Visa and E-1 Visa – How to Become “Legal” Entrepreneur in the U.S.</li>
    </ul>
  </section>

  <article class="product abs" style="left:14px">
    <div class="product-art art-ebook abs" role="img" aria-label="Illustration of an e-book"></div>
    <h4 class="abs">E BOOKS</h4>
    <p class="abs">olor sit amet conse ctetur adipisicing elit, sed do eiusmod tempor incididunt ut labore.</p>
    <a class="more abs" href="#">CLICK HERE</a>
  </article>
  <article class="product abs" style="left:240px">
    <div class="product-art art-brochure abs" role="img" aria-label="Illustration of an e-brochure"></div>
    <h4 class="abs">E-BROCHURES</h4>
    <p class="abs">olor sit amet conse ctetur adipisicing elit, sed do eiusmod tempor incididunt ut</p>
    <a class="more abs" href="#">CLICK HERE</a>
  </article>
  <article class="product abs" style="left:466px">
    <div class="product-art art-dvd abs" role="img" aria-label="Illustration of DVD discs"></div>
    <h4 class="abs">DVDS</h4>
    <p class="abs">olor sit amet conse ctetur adipisicing elit, sed do eiusmod tempor incididunt ut labore.</p>
    <a class="more abs" href="#">CLICK HERE</a>
  </article>

  <footer>
    <div class="footer-col abs" style="left:18px">
      <h5>WORK VISAS</h5>H1B Visa<br>I-Visa<br>O-Visa<br>P-Visa<br>Q-Visa<br>R-Visa<br>TN-Visa
    </div>
    <div class="footer-col abs" style="left:121px">
      <h5>BUSINESS VISAS</h5>Business Visa (B1)<br>Investor and Trader Visa (E)
      <h5 class="sub">CITIZENSHIP</h5>Green Card<br>Deportation
    </div>
    <div class="footer-col abs" style="left:257px">
      <h5 class="tight">FAMILY VISAS</h5><h5 class="tight">STUDENT VISAS</h5><h5 class="tight">VISITORS VISAS</h5><h5 class="tight">ESTA</h5><h5 class="tight">TOURIST VISA B1/B2</h5>
    </div>
    <div class="footer-col abs" style="left:390px">
      <h5>LINKS</h5>Partner Pages<br>Dubrik &amp; Helmsley<br>Meridian Foundation<br>Incorporate Company LLC Ltd. in<br>USA England Hong Kong or Offshore
    </div>
    <div class="footer-col abs" style="left:579px">
      <h5>CONTACTS</h5>Dubrik &amp; Helmsley<br>New York<br>48 W 71st Street #4C<br>New York 10023 NY<br>+1 (212) 555-0147
    </div>
    <div class="footer-rule abs"></div>
    <div class="legal abs">All Rights Reserved © 2012 | Dubrik &amp; Helmsley | Terms of Use and Privacy Policy</div>
    <div class="social abs">
      <span style="background:#3b5a98"></span><span style="background:#4cb4e6"></span><span style="background:#1f6fa8"></span><span style="background:#f08a24"></span><span style="background:#5aa84a"></span>
    </div>
  </footer>
</div>
</body>
</html>
```